Liquor Label / Aguardiente

Label design for liquor bottle. Designers may submit multiple submissions.

Product Description:
Name: Luna de Cobre™
Alcohol Category: Aguardiente (which in Spanish most closely translates to “burning water”) – aguardiente is derived from
cane sugar and is a general term for a type of alcoholic spirit in many Central and South America countries.
Taste: A smooth liquor with a comfortable yet spicy finish
Smell: Subtle aroma of spicy jalapeños
Liquid Color: Clear
Bottle Color: Clear
See link for reference - http://www.pellowinery.example/sites/default/files/styles/uc_product_full/public/Vessel_0.jpg?itok=8KqTm2Xw
Closure: Bar top / cork
Bottle Shape/Size: height = 8.67in; diameter of base = 3.70in; diameter of neck = 0.85in

Label may consist of two separate parts (i.e. front and back, front and vertical side), or one continuous label.

Designer has complete freedom with color, font etc. unless otherwise stated below. The label MUST
contain (but is not limited only to) the following text exactly as written in quotes below:
- “Luna de Cobre”
- “Aguardiente”
- “Cane Neutral Spirit with Natural Flavors”
- “35% Alc./Vol.”
- “750 ml”
- “Bottled by QM Spirits, LLC” and “Alder Falls, KY” - “Government Warning: (1) According to the Surgeon General, women should not drink alcoholic beverages during
pregnancy because of the risk of birth defects. (2) Consumption of alcoholic beverages impairs your ability to
drive a car or operate machinery, and may cause health problems.” (text in previous quotes must be in all
capitalized letters, text must be 2 MM in height and quote must be separated 2MM by all other text)
- Must be dedicated empty space for bar code (approximately 0.75in. height x 1.25in. length)
Updates

Target Market(s)

Label should have mass market appeal.
Age: 21 – 28 years old (primary target market is 21+ year old college students and recent graduates)
Target Market Gender: Both male and female, with emphasis on male
Consumption Focus: Spirit will be consumed typically as a shot, primarily at bars and secondarily off premise (label design will be critical for making our product highly visible behind a bar)
Marketing Theme: South American elements. The official Luna de Cobre mascot is a llama and the incorporation and use of a llama somewhere (however large or small) on the bottle is encourage but by no means required.

Industry/Entity Type

Health

Requirements
Should not have
• Elements that may lead a potential consumer to believe the beverage is a craft liquor or an artisan brand. Please do not include images of peppers.

```html
<!DOCTYPE html>
<html lang="en">
<head>
<meta charset="utf-8">
<title>Luna de Cobre — Aguardiente Label</title>
<link rel="stylesheet" href="https://fonts.googleapis.com/css2?family=Archivo+Black&family=Arimo:wght@400&family=Inter:wght@300&family=Libre+Baskerville:ital@1&family=Carlito&display=swap">
<style>
  :root {
    --ink: #0000cc;
    --band: #0000d2;
    --frame: #0a10d0;
    --sky: #4d8af0;
    --cyan: #5ee4ee;
    --paper: #ffffff;
  }
  html, body {
    margin: 0;
    padding: 0;
    width: 1109px;
    height: 1200px;
    overflow: hidden;
    background: var(--paper);
  }
  .canvas {
    position: relative;
    width: 1109px;
    height: 1200px;
    overflow: hidden;
    background: var(--paper);
  }
  .label {
    position: absolute;
    left: 0;
    top: 0;
    width: 1061px;
    height: 1152px;
    transform: scale(1.0417);
    transform-origin: top left;
    color: var(--ink);
    font-family: "Arimo", Arial, sans-serif;
  }
  .label__frame {
    position: absolute;
    left: 12px;
    top: 12px;
    width: 1029px;
    height: 1119px;
    border: 3px solid var(--frame);
  }
  .brand-name {
    position: absolute;
    left: 63px;
    top: 85px;
    margin: 0;
    font-family: "Archivo Black", "Arial Black", sans-serif;
    font-size: 56px;
    line-height: 56px;
    font-weight: 400;
    letter-spacing: 2.4px;
    white-space: nowrap;
    color: var(--ink);
  }
  .divider {
    position: absolute;
    left: 636px;
    top: 82px;
  }
  .category {
    position: absolute;
    left: 673px;
    top: 85px;
    font-family: "Inter", Helvetica, sans-serif;
    font-weight: 300;
    font-size: 58px;
    line-height: 58px;
    white-space: nowrap;
    color: var(--sky);
  }
  .tasting-note {
    position: absolute;
    left: 60px;
    top: 167px;
    margin: 0;
    font-family: "Libre Baskerville", Georgia, serif;
    font-style: italic;
    font-size: 26px;
    line-height: 46px;
    white-space: nowrap;
    color: var(--ink);
  }
  .translation {
    position: absolute;
    left: 0;
    top: 321px;
    width: 1061px;
    text-align: center;
    font-size: 21px;
    line-height: 21px;
    color: var(--sky);
  }
  .spec-band {
    position: absolute;
    left: 12px;
    top: 367px;
    width: 1035px;
    height: 50px;
    background: var(--band);
    color: var(--paper);
    font-size: 28px;
    line-height: 50px;
  }
  .spec-band__abv { position: absolute; left: 54px; top: 0; }
  .spec-band__volume { position: absolute; right: 54px; top: 0; }
  .gov-warning {
    position: absolute;
    left: 72px;
    top: 454px;
    margin: 0;
    font-size: 30px;
    line-height: 46px;
    letter-spacing: 1.2px;
    white-space: nowrap;
    color: var(--ink);
  }
  .gov-warning span { display: block; }
  .gov-warning .gap { height: 46px; }
  .barcode-space {
    position: absolute;
    left: 72px;
    top: 862px;
    width: 370px;
    height: 219px;
    border: 3px solid var(--cyan);
    display: flex;
    align-items: center;
    justify-content: center;
    font-family: "Carlito", Calibri, sans-serif;
    font-size: 50px;
    color: var(--cyan);
  }
  .bottler {
    position: absolute;
    left: 531px;
    top: 911px;
    margin: 0;
    font-size: 30px;
    line-height: 46px;
    letter-spacing: 1.2px;
    white-space: nowrap;
    color: var(--ink);
  }
</style>
</head>
<body>
<div class="canvas">
  <div class="label">
    <div class="label__frame"></div>

    <h1 class="brand-name">LUNA DE COBRE</h1>
    <svg class="divider" width="6" height="70" viewBox="0 0 6 70" aria-hidden="true">
      <path d="M3 1 Q5.5 35 3 69 Q0.5 35 3 1 Z" fill="var(--ink)"/>
    </svg>
    <div class="category">Aguardiente</div>

    <p class="tasting-note">A smooth liquor with a comfortable yet spicy finish and<br>subtle aroma of spicy jalapenos made from Cane Neutral<br>Spirit with Natural Flavors.</p>

    <div class="translation">[Aguardiente] - spanish for “burning water”.</div>

    <div class="spec-band">
      <span class="spec-band__abv">35% Alc./Vol.</span>
      <span class="spec-band__volume">750 ml</span>
    </div>

    <p class="gov-warning">
      <span>“GOVERNMENT WARNING:</span>
      <span>(1) ACCORDING TO THE SURGEON GENERAL, WOMEN</span>
      <span>SHOULD NOT DRINK ALCOHOLIC BEVERAGES DURING</span>
      <span>PREGNANCY BECAUSE OF THE RISK OF BIRTH DEFECTS.</span>
      <span class="gap"></span>
      <span>(2) CONSUMPTION OF ALCOHOLIC BEVERAGES IMPAIRS</span>
      <span>YOUR ABILITY TO DRIVE A CAR OR OPERATE MACHINERY,</span>
      <span>AND MAY CAUSE HEALTH PROBLEMS.”</span>
    </p>

    <div class="barcode-space">bar code area</div>

    <p class="bottler">Bottled by ”QM SPIRITS, LLC”<br>and “ALDER FALLS, KY”</p>
  </div>
</div>
</body>
</html>
```